Create a pouch design for a new sports supplement product

Dimensions are 235mm (width) x 335mm (length) x 110mm (gusset)
File 1 - Extension of design brief please read both briefs
File 2 - Is 2 potential pouches this is just to give you a better example of size the dimensions are for the pouch on the right. This picture is not to give you design ideas as I am not very keen on either of these designs.
We need a design to be printed onto the pouches of our whey protein product. The brand name is 'Stellar Fuelworks' and needs to be displayed on the packaging either just writing or a simple logo design. I am not the most creative person in the world but have put together a more detailed brief listing some of the key information that needs to be included on the pouch (See attachment) Please feel free if you have experience of this the sports supplement market or have different ideas then please feel free to explore them.
The pouch would either be printed straight onto the pouch, or possibly just a printed label (front & back) to be stuck onto the pouch. Please design either or both.
Open to different colour schemes. Design has to be modern looking and eye-catching.
Some key points;
High quality whey protein concentrate
All Natural
Soy free
Great tasting
Please google image search 'protein pouches' to see other designs if your not familiar with the sports supplement market.
Any questions feel free to ask.
Updates
Hi, Thanks for all your design! I am really busy at the moment so haven't had chance to give feedback and have a proper look through all the designs. I have extended the time frame to give myself chance to give proper feedback and see any changes needed. Expect feedback sunday at the latest, and I will be pick a design early next week.
Target Market(s)
Sports supplement market. Product is a whey protein shake
Industry/Entity Type
Nutrition
Look and feel
Each slider illustrates characteristics of the customer's brand and the style your logo design should communicate.

```html
<!DOCTYPE html>
<html lang="en">
<head>
<meta charset="utf-8">
<title>Stellar Fuelworks – Natural Whey Protein Pouch</title>
<link rel="stylesheet" href="https://fonts.googleapis.com/css2?family=Exo+2:wght@800;900&family=Fira+Sans:wght@500;600;700&display=swap">
<style>
  :root {
    --backdrop: #d6d6d6;
    --pouch-black: #0d0b0b;
    --pouch-deep: #1a0707;
    --glow-red: #8a1010;
    --brand-red: #e5141a;
    --brand-red-bright: #ff2a1f;
    --silver: #e4e4e4;
    --white: #ffffff;
  }
  * { margin: 0; padding: 0; box-sizing: border-box; }
  html, body {
    width: 1200px; height: 900px; overflow: hidden;
    background: var(--backdrop);
  }
  .canvas { position: relative; width: 1200px; height: 900px; }

  .pouch {
    position: absolute; left: 410px; top: 130px;
    width: 445px; height: 690px;
    background: var(--pouch-black);
    overflow: hidden;
    font-family: "Fira Sans", sans-serif;
    color: var(--white);
  }
  .pouch-pattern {
    position: absolute; inset: 0;
    background:
      radial-gradient(ellipse 60% 45% at 50% 48%, var(--glow-red) 0%, rgba(120,10,10,0.55) 45%, transparent 80%),
      linear-gradient(180deg, var(--pouch-deep) 0%, #3a0909 40%, #2a0808 70%, var(--pouch-black) 100%);
  }

  .tear-band {
    position: absolute; left: 0; top: 53px; width: 100%; height: 34px;
    background: var(--brand-red);
    display: flex; align-items: center; justify-content: flex-end;
    padding-right: 22px;
    font-size: 14px; font-weight: 600; letter-spacing: 2px;
  }

  .brand-word {
    position: absolute; width: 400px; height: 58px;
    transform-origin: left top; transform: rotate(-90deg);
    text-align: right;
    font-family: "Exo 2", sans-serif; font-weight: 900;
    font-size: 62px; line-height: 58px; letter-spacing: 1px;
    color: var(--silver);
    white-space: nowrap;
  }
  .brand-word--first { left: 56px; top: 560px; }
  .brand-word--second { left: 122px; top: 560px; }

  .divider {
    position: absolute; left: 202px; top: 160px;
    width: 1px; height: 400px; background: rgba(255,255,255,0.55);
  }

  .product-info { position: absolute; left: 220px; top: 212px; }
  .product-name { font-size: 31px; font-weight: 600; line-height: 39px; }

  .tag {
    display: inline-block;
    background: var(--brand-red-bright);
    clip-path: polygon(0 0, calc(100% - 14px) 0, 100% 50%, calc(100% - 14px) 100%, 0 100%);
    font-weight: 700; white-space: nowrap;
  }
  .tag--flavour {
    margin-top: 10px; height: 22px; line-height: 22px;
    padding: 0 30px 0 5px; font-size: 14px; letter-spacing: 0.5px;
  }

  .quantity { display: flex; align-items: flex-end; margin-top: 20px; gap: 18px; }
  .servings-count { font-family: "Exo 2", sans-serif; font-weight: 800; font-size: 44px; line-height: 40px; }
  .servings-label { font-size: 12px; font-weight: 600; letter-spacing: 0.5px; margin-top: 4px; }
  .net-weight { font-family: "Exo 2", sans-serif; font-weight: 800; font-size: 22px; margin-bottom: 20px; }

  .benefits { list-style: none; margin-top: 20px; }
  .benefits .tag {
    display: block; width: fit-content;
    height: 17px; line-height: 17px; margin-bottom: 4px;
    padding: 0 20px 0 5px; font-size: 11px; font-weight: 600;
  }
</style>
</head>
<body>
<main class="canvas">
  <section class="pouch">
    <div class="pouch-pattern" role="img" aria-label="Dark red hexagon honeycomb pattern with a central red glow"></div>

    <div class="tear-band">TEAR HERE &amp; RESEAL</div>

    <h1 class="brand-name">
      <span class="brand-word brand-word--first">STELLAR</span>
      <span class="brand-word brand-word--second">FUELWORKS</span>
    </h1>

    <div class="divider"></div>

    <div class="product-info">
      <h2 class="product-name">Natural<br>Whey Protein</h2>
      <div class="tag tag--flavour">STRAWBERRY FLAVOUR</div>

      <div class="quantity">
        <div class="servings">
          <div class="servings-count">30</div>
          <div class="servings-label">SERVINGS</div>
        </div>
        <div class="net-weight">909g</div>
      </div>

      <ul class="benefits">
        <li class="tag">No artificial Flavours</li>
        <li class="tag">Excellent Amino acid profile</li>
        <li class="tag">80% high quality protein content</li>
        <li class="tag">Soy free</li>
      </ul>
    </div>
  </section>
</main>
</body>
</html>
```